Business Card Bright Willow Path
Professional
Marla Quennby, ACC, MSc, DipC
Founder
HTMA Administration Office
PO Box 27381
Birmingham
B47 3KT
info@brightwillowpath.co.uk
brightwillowpath.co.uk
Please use both variations of the logo while submitting design.
Business cards to look modern, fresh, feminine, in alignment with logo branding.
Small print to say: a division of The Harbor Trust For Mentoring Ambition
Colour scheme, images and writting to co ordinate with logo.
I do not want the address on the business cards
The market for these cards is proffessional women hence a modern, proffessional yet not too corporate and not "woo woo".
I do not want the address on the business cards.

```html
<!DOCTYPE html>
<html lang="en">
<head>
<meta charset="utf-8">
<title>Bright Willow Path — Business Cards</title>
<link href="https://fonts.googleapis.com/css2?family=Cinzel:wght@400;600&family=Cormorant+Garamond:ital,wght@0,500;0,600;1,500;1,600&family=Open+Sans:wght@400&display=swap" rel="stylesheet">
<style>
  :root{
    --bg:#3b2b23;
    --card:#ffffff;
    --red:#c8222c;
    --deep-red:#9e1c2a;
    --orange:#f27c2c;
    --pale:#f6d9d6;
    --ink:#5a4a48;
    --white:#ffffff;
    --label:#f3ece6;
  }
  *{box-sizing:border-box;margin:0;padding:0}
  html,body{width:1200px;height:746px;overflow:hidden;background:var(--bg)}
  .canvas{position:relative;width:1200px;height:746px}
  .side-label{position:absolute;top:8px;font-family:"Open Sans",sans-serif;font-size:34px;color:var(--label);width:504px;text-align:center}
  .card{position:absolute;width:504px;height:300px;border-radius:16px;overflow:hidden}
  .card--front{background:var(--card);top:67px}
  .card--back{top:378px;background:radial-gradient(ellipse at 50% 55%,var(--orange) 0%,#e4512a 45%,var(--red) 100%)}
  .pos-left{left:72px}
  .pos-right{left:619px}
  .brand{font-family:"Cinzel",serif;font-weight:400;letter-spacing:.5px;white-space:nowrap}
  .tagline{font-family:"Cormorant Garamond",serif;font-style:italic;font-weight:600;color:var(--red);text-align:center;position:absolute;left:0;right:0;white-space:nowrap}

  /* Front 1 */
  .faint-brand{position:absolute;top:52px;left:0;right:0;text-align:center;font-size:30px;color:var(--pale)}
  .person{position:absolute;left:36px;top:168px;color:var(--deep-red)}
  .person__name{font-family:"Cinzel",serif;font-size:19px;letter-spacing:.3px}
  .person__creds,.person__role{font-family:"Cinzel",serif;font-size:13px;color:var(--ink);margin-top:3px}
  .divider{position:absolute;left:257px;top:158px;width:1px;height:86px;background:#c9b9b7}
  .contacts{position:absolute;left:272px;top:158px;list-style:none}
  .contacts li{display:flex;align-items:center;gap:8px;font-family:"Cormorant Garamond",serif;font-weight:600;font-size:15px;color:var(--deep-red);height:21px}
  .contacts svg{width:12px;height:12px;flex:none}
  .card1-tag{top:258px;font-size:18px}

  /* Front 2 */
  .mark-dot{position:absolute;left:227px;top:30px;width:50px;height:50px;border-radius:50%;background:var(--red)}
  .front2-brand{position:absolute;top:118px;left:0;right:0;text-align:center;font-size:31px;color:var(--red)}
  .card2-tag{top:160px;font-size:17px}
  .front2-name{position:absolute;top:196px;left:0;right:0;text-align:center;font-family:"Cinzel",serif;font-size:17px;color:var(--red);white-space:nowrap}
  .front2-name small{font-family:"Cormorant Garamond",serif;font-size:14px;color:var(--ink);font-weight:600}
  .front2-row{position:absolute;left:0;right:0;display:flex;justify-content:center;gap:26px;font-family:"Cormorant Garamond",serif;font-weight:600;font-size:14px;color:var(--ink);white-space:nowrap}
  .front2-row span{display:flex;align-items:center;gap:6px}
  .front2-row svg{width:11px;height:11px}
  .row-phones{top:224px}
  .row-web{top:248px}

  /* Backs */
  .back-mark{position:absolute;left:222px;top:60px;width:60px;height:60px;border-radius:50%;background:rgba(255,255,255,.92)}
  .back-brand{position:absolute;top:160px;left:0;right:0;text-align:center;font-size:34px;color:var(--white)}
  .back-tag{position:absolute;top:204px;left:0;right:0;text-align:center;font-family:"Cormorant Garamond",serif;font-style:italic;font-weight:600;font-size:17px;color:var(--white);white-space:nowrap}
  .back-web{position:absolute;bottom:18px;left:0;right:0;text-align:center;font-family:"Cormorant Garamond",serif;font-weight:600;font-size:16px;letter-spacing:2px;color:var(--white)}
  .big-mark{position:absolute;left:202px;top:36px;width:100px;height:100px;border-radius:50%;background:rgba(255,255,255,.95)}
  .big-brand{position:absolute;top:150px;left:0;right:0;text-align:center;font-size:40px;color:var(--white)}
</style>
</head>
<body>
<main class="canvas">
  <div class="side-label pos-left">Front 1</div>
  <div class="side-label pos-right">Front 2</div>

  <section class="card card--front pos-left">
    <div class="faint-brand brand">Bright Willow Path</div>
    <div class="person">
      <div class="person__name">Marla Quennby</div>
      <div class="person__creds">ACC, MSc, DipC</div>
      <div class="person__role">Founder</div>
    </div>
    <div class="divider"></div>
    <ul class="contacts">
      <li><svg viewBox="0 0 12 12"><circle cx="6" cy="6" r="6" fill="#9e1c2a"/><path d="M4 3.2l1 1.4-.6.7c.4.9 1 1.5 1.9 1.9l.7-.6 1.4 1-.5 1C6 8.4 3.6 6 3.3 4z" fill="#fff"/></svg>+44 (0) 161 496 0723</li>
      <li><svg viewBox="0 0 12 12"><circle cx="6" cy="6" r="6" fill="#9e1c2a"/><rect x="4.3" y="2.6" width="3.4" height="6.8" rx=".6" fill="#fff"/></svg>+44 (0) 7700 90 31 62</li>
      <li><svg viewBox="0 0 12 12"><circle cx="6" cy="6" r="6" fill="#9e1c2a"/><rect x="3" y="4" width="6" height="4.2" fill="#fff"/><path d="M3 4l3 2.3L9 4" stroke="#9e1c2a" stroke-width=".7" fill="none"/></svg>info@brightwillowpath.co.uk</li>
      <li><svg viewBox="0 0 12 12"><circle cx="6" cy="6" r="6" fill="#9e1c2a"/><circle cx="6" cy="6" r="3" fill="none" stroke="#fff" stroke-width=".8"/><path d="M3 6h6M6 3v6" stroke="#fff" stroke-width=".7"/></svg>www.brightwillowpath.co.uk</li>
    </ul>
    <p class="tagline card1-tag">renew your purpose, steady your path and lift your heart</p>
  </section>

  <section class="card card--front pos-right">
    <div class="mark-dot"></div>
    <div class="front2-brand brand">Bright Willow Path</div>
    <p class="tagline card2-tag">renew your purpose, steady your path and lift your heart</p>
    <div class="front2-name">Marla Quennby <small>(ACC, MSc, DipC)</small> Founder</div>
    <div class="front2-row row-phones">
      <span><svg viewBox="0 0 12 12"><path d="M2.5 1.5l2 2.6-1 1.2c.8 1.6 1.6 2.4 3.2 3.2l1.2-1 2.6 2-1 1.5C5.5 10.8 1.2 6.5 1 2.5z" fill="#c8222c"/></svg>+ 44 (0) 161 496 0723</span>
      <span><svg viewBox="0 0 12 12"><rect x="3.5" y="1" width="5" height="10" rx="1" fill="#c8222c"/></svg>+ 44 (0) 7700 90 31 62</span>
    </div>
    <div class="front2-row row-web">
      <span><svg viewBox="0 0 12 12"><rect x="1" y="2.5" width="10" height="7" fill="#c8222c"/><path d="M1 2.5l5 4 5-4" stroke="#fff" stroke-width=".9" fill="none"/></svg>info@brightwillowpath.co.uk</span>
      <span><svg viewBox="0 0 12 12"><circle cx="6" cy="6" r="5" fill="none" stroke="#c8222c" stroke-width="1.2"/><path d="M1 6h10M6 1v10" stroke="#c8222c" stroke-width="1"/></svg>www.brightwillowpath.co.uk</span>
    </div>
  </section>

  <section class="card card--back pos-left">
    <div class="back-mark"></div>
    <div class="back-brand brand">Bright Willow Path</div>
    <p class="back-tag">renew your purpose, steady your path and lift your heart</p>
    <div class="back-web">www.brightwillowpath.co.uk</div>
  </section>

  <section class="card card--back pos-right">
    <div class="big-mark"></div>
    <div class="big-brand brand">Bright Willow Path</div>
    <div class="back-web">www.brightwillowpath.co.uk</div>
  </section>
</main>
</body>
</html>
```